Priority Goals poster for school year

We are an elementary school and the past two years have had you help us to design a "poster" that illustrates our goal of the coming year. I am attaching our last year's one, along with some photos of our (ver rough) thinking for next years. The priority goal at top remains the same. Can't wait to see your genius ideas! :)

Target Market(s)

Staff of an elementary school and parents to some (informative) extent as well.

Colors
296eb1
6094c6
fbed22
fbee3f

Requirements
Must have
• items from the white board picture we have attached

```html
<!DOCTYPE html>
<html lang="en">
<head>
<meta charset="utf-8">
<title>Cedarline Elementary School – 2020-2021 Priority Goals</title>
<link href="https://fonts.googleapis.com/css2?family=Montserrat:wght@300;400;600;700;800&family=Bebas+Neue&display=swap" rel="stylesheet">
<style>
  :root{
    --blue:#2f7fca;
    --blue-deep:#296eb1;
    --blue-soft:#6094c6;
    --yellow:#fbed22;
    --yellow-soft:#fbee3f;
    --ink:#1d1d1f;
    --paper:#ffffff;
    --ring:#dbe8f5;
  }
  *{box-sizing:border-box;margin:0;padding:0}
  html,body{width:900px;height:1200px;overflow:hidden;background:var(--paper)}
  .poster{position:relative;width:900px;height:1200px;background:var(--paper);font-family:"Montserrat",sans-serif}

  .school-name{position:absolute;left:64px;top:70px;width:260px;display:flex;align-items:center;gap:14px;
    color:var(--blue-deep);font-weight:800;font-size:26px;line-height:1.1;text-transform:uppercase}
  .school-name .mark{flex:none;width:56px;height:56px;border-radius:50%;background:var(--yellow)}

  .headline{position:absolute;right:62px;top:66px;text-align:right}
  .headline .year{color:var(--blue);font-weight:800;font-size:76px;line-height:1;letter-spacing:1px}
  .headline .title{color:var(--ink);font-weight:800;font-size:45px;line-height:1.15;letter-spacing:1px}

  .pillars{position:absolute;left:64px;top:268px;width:772px;display:flex;gap:10px}
  .pillar{flex:1;height:72px;border-radius:8px;background:var(--blue-soft);color:#fff;
    font-weight:700;font-size:16px;line-height:1.3;display:flex;align-items:center;justify-content:center;text-align:center;letter-spacing:.5px}

  .goal-wheel{position:absolute;left:170px;top:366px;width:560px;height:560px}
  .goal-label{position:absolute;font-size:11px;line-height:1.4;color:#fff;white-space:nowrap}
  .goal-label b{display:block;color:var(--yellow);font-weight:700;font-size:14px;margin-bottom:3px}
  .wheel-center{position:absolute;left:0;width:100%;text-align:center;font-family:"Bebas Neue",sans-serif;
    color:var(--blue);font-size:50px;line-height:.98}

  .promise{position:absolute;left:0;width:100%;top:948px;text-align:center}
  .promise .line-one{font-family:"Bebas Neue",sans-serif;color:var(--blue);font-size:66px;line-height:1}
  .promise .line-two{font-weight:400;color:var(--ink);font-size:38px;letter-spacing:2px;line-height:1.1}

  .contact-band{position:absolute;left:0;bottom:0;width:900px;height:110px}
  .contact-band .band-shape{position:absolute;left:0;top:0}
  .phone{position:absolute;left:54px;top:30px;display:flex;align-items:center;gap:14px;color:#fff;
    font-family:"Bebas Neue",sans-serif;font-size:60px;line-height:1}
  .phone .phone-icon{flex:none;display:block}
  .handle{position:absolute;left:510px;top:22px;display:flex;align-items:center;gap:12px;color:var(--ink);font-weight:600;font-size:26px}
  .handle .dot{width:24px;height:24px;border-radius:5px;background:var(--blue)}
</style>
</head>
<body>
<main class="poster">

  <div class="school-name"><span class="mark"></span><span>Cedarline Elementary School</span></div>

  <header class="headline">
    <div class="year">2020-2021</div>
    <div class="title">PRIORITY GOALS</div>
  </header>

  <section class="pillars">
    <div class="pillar">Be intentiomal with<br>padr actor-focus</div>
    <div class="pillar">Staff douing what they<br>love teaching</div>
    <div class="pillar">Mental health for<br>every pesos</div>
  </section>

  <section class="goal-wheel">
    <svg width="560" height="560" viewBox="0 0 560 560">
      <circle cx="280" cy="280" r="275" fill="var(--blue)"/>
      <circle cx="280" cy="270" r="108" fill="#fff"/>
      <g fill="#fff" stroke="var(--ring)" stroke-width="5">
        <circle cx="283" cy="86" r="68"/>
        <circle cx="473" cy="273" r="68"/>
        <circle cx="272" cy="456" r="68"/>
        <circle cx="88" cy="260" r="68"/>
      </g>
      <g fill="var(--yellow)">
        <circle cx="283" cy="94" r="22"/>
        <circle cx="283" cy="94" r="9" fill="#fff"/>
        <circle cx="266" cy="64" r="7"/><circle cx="283" cy="60" r="7"/><circle cx="300" cy="64" r="7"/>
        <rect x="447" y="252" width="42" height="30" rx="4"/>
        <path d="M456 282 l0 10 l10 -10z"/>
        <rect x="463" y="264" width="36" height="26" rx="4" fill="#f3c611"/>
        <path d="M88 240 l18 10 v20 l-18 10 l-18 -10 v-20z"/>
        <path d="M60 228 v60 h62" fill="none" stroke="var(--yellow)" stroke-width="3"/>
        <path d="M265 428 l20 22 h-12 v26 h-16 v-26 h-12z"/>
        <circle cx="292" cy="470" r="11"/>
        <path d="M286 470 l4 4 l8 -8" fill="none" stroke="#fff" stroke-width="3"/>
      </g>
    </svg>
    <div class="wheel-center" style="top:222px">PRIORITY<br>GOALS</div>
    <div class="goal-label" style="left:92px;top:100px"><b>Voices of all</b>Who we are?<br>Where are we going</div>
    <div class="goal-label" style="left:392px;top:128px"><b>Comunicate</b>Eypectahare<br>Support<br>Far clority</div>
    <div class="goal-label" style="left:58px;top:352px"><b>Small measured</b>Step towards biger<br>goal</div>
    <div class="goal-label" style="left:358px;top:380px"><b>Build value</b>Connect<br>Celebrate<br>Strange pecdialis<br>Large hue fan</div>
  </section>

  <section class="promise">
    <div class="line-one">FOUNDATIONAL PROMISES 4 YEARS</div>
    <div class="line-two">STRONG BETTER EVERYDAY</div>
  </section>

  <footer class="contact-band">
    <svg class="band-shape" width="900" height="110" viewBox="0 0 900 110">
      <rect width="900" height="110" fill="var(--blue)"/>
      <path d="M440 16 H900 V74 H500 C480 74 470 60 460 40 C452 26 448 16 440 16z" fill="var(--yellow)"/>
      <path d="M0 0 H440 C448 0 452 8 456 16 H0z" fill="var(--paper)"/>
    </svg>
    <div class="phone">
      <svg class="phone-icon" width="36" height="36" viewBox="0 0 24 24"><path fill="#fff" d="M6.6 10.8a15 15 0 0 0 6.6 6.6l2.2-2.2a1 1 0 0 1 1-.25 11.4 11.4 0 0 0 3.6.57 1 1 0 0 1 1 1V20a1 1 0 0 1-1 1A17 17 0 0 1 3 4a1 1 0 0 1 1-1h3.5a1 1 0 0 1 1 1c0 1.25.2 2.45.57 3.57a1 1 0 0 1-.25 1z"/></svg>
      <span>555-014-2200</span>
    </div>
    <div class="handle"><span class="dot"></span><span>@cedarlinelearner</span></div>
  </footer>

</main>
</body>
</html>
```